Talented energy healer needs business card design

I need a business card design for a new energy healing business in Perth Australia. As an energy healer I am quite earthy and practical rather than floaty and fairydust.
One of the techniques I use is unique in Australia but used internationally (US, UK and Europe). I practice with Coastal Pathway Therapy, Reiki and massage as well as some other techniques I developed personally. I am starting to incorporate sound healing into my practice. I literally change people's lives. The potential for each client is wide open. A key skill I bring to my practice is the capacity for making difficult situations seem more fun and less stressful.
Clients are likely to be depressed, physically unwell, going through a difficult time, unhappy with their current situation. They are people looking for new options to solve a difficult existing problem. They have probably tried other avenues before they come to me. They are open to something different.

I would like to communicate that the client and I work together for their healing and personal growth. I would like to convey that while the work of changing is challenging it can also be fun.

Hi all, info required on the card is:

Name
Title: Healer
contact number (mobile)
I don''t have a logo - I would be interested in seeing designs that use the whole card as well as the traditional logo on one side / in one corner. Whatever ''look/feel'' I choose will carry over to the website as well.

thanks
Meg

Reason: One or two of the designs caught my eye and many appeal for different reasons, but nothing is quite right for me. I've invited a couple of other designers to contribute so I wanted to give them time to be involved. kind regards Meg

Thank you all for the fabulous designs. I really appreciated the thought that many people put into my brief and a number of designs captured important things about what I was trying to say. It was a hard choice between 3 designs in the end.
thanks again and kind regards
Meg

Target Market(s)

people looking for new options to solve a difficult existing problem

Industry/Entity Type

Massage

Logo styles of interest
Abstract Logo
Requirements
Must have
• include green and blue
Nice to have
• hands, tea / teapots , the ocean, stepping stones

```html
<!DOCTYPE html>
<html lang="en">
<head>
<meta charset="utf-8">
<title>Meg, Healer – Business Card</title>
<link rel="stylesheet" href="https://fonts.googleapis.com/css2?family=Comic+Neue:wght@700&family=Open+Sans:wght@400&family=Arimo:wght@700&display=swap">
<style>
  :root {
    --page-bg: #ecebe8;
    --card-bg: #ffffff;
    --name-green: #0a6a12;
    --title-blue: #19a3e0;
    --text-grey: #555555;
    --list-grey: #5f5f5f;
    --guild-navy: #1d2f7a;
    --stone-sand: #d9c29a;
    --stone-grey: #7d8690;
    --steps-orange: #f07a2a;
    --steps-blue: #3d7fc4;
    --teapot-cream: #ece6dc;
    --teapot-grey: #b9b4ad;
  }
  * { box-sizing: border-box; margin: 0; padding: 0; }
  html, body { width: 1200px; height: 692px; overflow: hidden; }
  body {
    background: var(--page-bg);
    font-family: "Open Sans", Arial, sans-serif;
    position: relative;
  }
  .card {
    position: absolute;
    top: 186px;
    width: 540px;
    height: 320px;
    background: var(--card-bg);
    border-radius: 22px;
    overflow: hidden;
    box-shadow: 0 6px 18px rgba(0,0,0,0.18);
  }
  .card--front { left: 40px; }
  .card--back { left: 620px; }

  .front__photo {
    position: absolute;
    left: 0; top: 0; bottom: 0;
    width: 190px;
    background: linear-gradient(160deg, var(--stone-grey) 0%, #a8a49b 35%, var(--stone-sand) 70%, #c9ad80 100%);
  }
  .front__info {
    position: absolute;
    left: 190px; right: 0; top: 0; bottom: 0;
    text-align: center;
    color: var(--text-grey);
  }
  .front__heading {
    font-family: "Comic Neue", "Comic Sans MS", cursive;
    font-weight: 700;
    margin-top: 30px;
    line-height: 1;
  }
  .front__name { color: var(--name-green); font-size: 52px; }
  .front__title { color: var(--title-blue); font-size: 32px; }

  .guild {
    display: inline-flex;
    align-items: center;
    gap: 8px;
    font-family: "Open Sans", Arial, sans-serif;
    font-size: 13px;
    color: var(--guild-navy);
  }
  .guild__dot {
    width: 54px; height: 54px;
    border-radius: 50%;
    background: var(--guild-navy);
    flex: none;
  }
  .front__guild { margin-top: 22px; }

  .contact { margin-top: 22px; font-size: 14px; line-height: 1.7; }
  .contact__row { display: flex; justify-content: center; gap: 14px; align-items: center; }
  .contact__item { display: inline-flex; align-items: center; gap: 5px; }
  .contact__icon { width: 11px; height: 11px; fill: var(--text-grey); }
  .contact__address { margin-top: 8px; font-size: 14px; }

  .back__list {
    list-style: none;
    margin-top: 34px;
    text-align: center;
    font-family: "Arimo", Arial, sans-serif;
    font-weight: 700;
    font-size: 22px;
    color: var(--list-grey);
    line-height: 1.55;
  }
  .back__list li::before { content: "• "; font-size: 16px; vertical-align: 3px; }
  .back__row {
    display: flex;
    justify-content: center;
    align-items: center;
    gap: 34px;
    margin-top: 20px;
  }
  .back__photo {
    width: 72px; height: 72px;
    border-radius: 50%;
  }
  .back__photo--steps { background: linear-gradient(170deg, var(--steps-orange) 0%, #f3a15e 35%, #9dbbe0 60%, var(--steps-blue) 100%); }
  .back__photo--teapot { background: radial-gradient(circle at 50% 55%, var(--teapot-cream) 0%, #dcd5ca 55%, var(--teapot-grey) 100%); }
</style>
</head>
<body>
  <section class="card card--front">
    <div class="front__photo" role="img" aria-label="Photograph of smooth river stones engraved with healing symbols on sand"></div>
    <div class="front__info">
      <h1 class="front__heading"><span class="front__name">Meg,</span> <span class="front__title">Healer</span></h1>
      <div class="guild front__guild"><span class="guild__dot"></span><span>Harbour Sound Guild</span></div>
      <div class="contact">
        <div class="contact__row">
          <span class="contact__item"><svg class="contact__icon" viewBox="0 0 10 10"><rect x="2.5" y="0" width="5" height="10" rx="1"/></svg>+123-456-789</span>
          <span class="contact__item"><svg class="contact__icon" viewBox="0 0 10 10"><rect x="0" y="2" width="10" height="6.5" rx="0.8"/></svg>hello@meghealer.com</span>
        </div>
        <div class="contact__row">
          <span class="contact__item"><svg class="contact__icon" viewBox="0 0 10 10"><circle cx="5" cy="5" r="4.5"/></svg>www.meghealer.com</span>
        </div>
        <div class="contact__address">00, Complex name, Street, city 002</div>
      </div>
    </div>
  </section>

  <section class="card card--back">
    <ul class="back__list">
      <li>Coastal Pathway Therapy</li>
      <li>Reiki</li>
      <li>Massage</li>
      <li>Sound Healing</li>
    </ul>
    <div class="back__row">
      <div class="guild"><span class="guild__dot"></span><span>Harbour Sound Guild</span></div>
      <div class="back__photo back__photo--steps" role="img" aria-label="Photograph of stepping stones across blue water at sunset"></div>
      <div class="back__photo back__photo--teapot" role="img" aria-label="Photograph of a floral porcelain teapot"></div>
    </div>
  </section>
</body>
</html>
```